IT Company Business Card Rebranding

We want to modernize our business cards massively. We want to incorporate aspects of our old business card such as the white and geometric design with the blues of another icon. Existing Logo, old business card and icon are all attached.

We are a modern IT company that provides support for new and growing technologies and want our business cards to be modern yet professional.
Updates

Note: Do not use file ICON.png in design. This is just a design we like Added Wednesday, March 9, 2016

Industry/Entity Type

Information Technology

Contact Information for Business Card

Roughly 43 : 26 or 1075 x 650 px

Font styles to use
Serif

Colors
0492cd
3276b5
33a6d7
86cfc6
cfeae6
cee9f5
ffffff

Requirements
Must have
• Modern yet professional
Nice to have
• We would like to incorporate the blues of our existing logo and of the icon provided. Really like the design of the icon.
Should not have
• Too Decorative. Just simple and professional.
• Not have the circle icon, as it is a copyrighted icon, I just like the colors and the geometric design

```html
<!DOCTYPE html>
<html lang="en">
<head>
<meta charset="utf-8">
<title>Nexa Tech – Business Card</title>
<link rel="stylesheet" href="https://fonts.googleapis.com/css2?family=Poiret+One&family=Questrial&display=swap">
<style>
  :root {
    --page-bg: #e9ecef;
    --blue-deep: #3276b5;
    --blue-mid: #0492cd;
    --blue-light: #33a6d7;
    --teal: #1fb5b0;
    --mint: #86cfc6;
    --white: #ffffff;
    --ink: #4a4f55;
    --ink-soft: #6b7076;
    --rule: #8a8f95;
    --logo-blue: #3276b5;
  }
  * { margin: 0; padding: 0; box-sizing: border-box; }
  html, body {
    width: 1200px; height: 975px; overflow: hidden;
    background: var(--page-bg);
  }
  .card {
    position: absolute; left: 62px; top: 162px;
    width: 1075px; height: 650px;
    overflow: hidden;
    box-shadow: 0 10px 30px rgba(0,0,0,0.18);
  }
  .card-backdrop {
    position: absolute; inset: 0;
    background: linear-gradient(125deg, var(--blue-deep) 0%, var(--blue-mid) 30%, var(--teal) 55%, var(--blue-light) 75%, var(--blue-deep) 100%);
  }
  .card-circle {
    position: absolute; left: 50%; top: 50%;
    width: 820px; height: 820px;
    transform: translate(-50%, -50%);
    border-radius: 50%;
    background: var(--white);
  }
  .card-content {
    position: absolute; inset: 0;
    display: flex; flex-direction: column; align-items: center;
    font-family: "Questrial", sans-serif;
    color: var(--ink);
  }
  .brand {
    margin-top: 72px;
    display: flex; align-items: center; gap: 18px;
  }
  .brand-dot {
    width: 54px; height: 54px; border-radius: 50%;
    background: var(--logo-blue);
  }
  .brand-name {
    font-family: "Questrial", sans-serif;
    font-size: 40px; letter-spacing: 10px;
    color: var(--logo-blue);
    text-transform: uppercase;
  }
  .rule {
    height: 2px; background: var(--rule);
  }
  .rule-top { width: 330px; margin-top: 40px; align-self: flex-start; margin-left: 290px; }
  .person-name {
    font-family: "Poiret One", sans-serif;
    font-size: 84px; letter-spacing: 6px;
    margin-top: 14px; line-height: 1;
    color: var(--ink);
  }
  .person-role {
    font-size: 28px; letter-spacing: 2px;
    margin-top: 10px; text-transform: uppercase;
    color: var(--ink);
  }
  .contact-list {
    list-style: none; margin-top: 22px;
    font-size: 27px; line-height: 40px;
    color: var(--ink-soft);
    align-self: flex-start; margin-left: 360px;
  }
  .rule-bottom { width: 330px; margin-top: 26px; align-self: flex-end; margin-right: 290px; }
</style>
</head>
<body>
  <div class="card">
    <div class="card-backdrop" role="img" aria-label="Soft blue and teal geometric diamond pattern background"></div>
    <div class="card-circle"></div>
    <div class="card-content">
      <div class="brand">
        <span class="brand-dot"></span>
        <span class="brand-name">Nexa Tech</span>
      </div>
      <div class="rule rule-top"></div>
      <h1 class="person-name">MIRA</h1>
      <p class="person-role">Technical Services</p>
      <ul class="contact-list">
        <li>Phone: 9012345678</li>
        <li>Email: mira@nexatech.com</li>
        <li>www.nexatech.com</li>
      </ul>
      <div class="rule rule-bottom"></div>
    </div>
  </div>
</body>
</html>
```